Calm Rootwell Sticker Design for TRIM 9

ur business name is ' Calm Rootwell ' ( Logo attached ).
The Product is called ' Trim 9 ' It has six ingredients that need to be listed on the sticker - Chia, Turmeric, Ginger, Dandelion, Macha and Seaweed.
120 capsules in a packet.
I would like it to say the product is a ' Weight loss alternative ' ' all organic ingredients ' All natural '

The logo.

Project Deadline Extended Reason: I would love to see a few more designs please. I have also just guaranteed the project. Thank you. CALM ROOTWELL x Added Tuesday, October 31, 2017

Target Market(s)

Everyone.

Industry/Entity Type

Health And Wellness

Requirements
Must have
• ur business name is ' Calm Rootwell ' ( Logo attached ).
• The Product is called ' Trim 9 ' It has six ingredients that need to be listed on the sticker - Chia, Turmeric, Ginger, Dandelion, Macha and Seaweed.
• 120 capsules in a packet.
• I would like it to say the product is a ' Weight loss alternative ' ' all organic ingredients ' All natural '
• The logo.
Nice to have
• A catchy image symbolising nature.

```html
<!DOCTYPE html>
<html lang="en">
<head>
<meta charset="utf-8">
<title>Calm Rootwell – Trim 9 Label</title>
<link rel="stylesheet" href="https://fonts.googleapis.com/css2?family=Noto+Sans:wght@400;600&display=swap">
<style>
  :root {
    --page-bg: #ececec;
    --label-light: #f4f7dc;
    --label-mid: #d9ebaa;
    --label-edge: #9fcc5e;
    --brand-green: #3e9b3c;
    --frame-green: #2fa84a;
    --name-green: #3f5a24;
    --ink: #111a10;
    --band: rgba(110, 140, 70, 0.82);
    --band-text: #ffffff;
    --figure: rgba(80, 150, 120, 0.18);
  }
  html, body {
    margin: 0;
    width: 1200px;
    height: 927px;
    overflow: hidden;
    background: var(--page-bg);
  }
  .label {
    position: absolute;
    left: 50px;
    top: 243px;
    width: 1100px;
    height: 440px;
    overflow: hidden;
    background:
      radial-gradient(ellipse 55% 70% at 55% 55%, var(--label-light) 0%, var(--label-mid) 55%, var(--label-edge) 100%);
    font-family: "Noto Sans", Verdana, sans-serif;
    color: var(--ink);
  }
  .leaf-canopy {
    position: absolute;
    left: 0;
    top: 0;
    width: 100%;
    height: 90px;
    background: linear-gradient(180deg, rgba(125, 187, 74, 0.55) 0%, rgba(125, 187, 74, 0) 100%);
  }
  .figure-area {
    position: absolute;
    left: 230px;
    top: 60px;
    width: 140px;
    height: 333px;
    background: linear-gradient(180deg, rgba(80, 150, 120, 0) 0%, var(--figure) 40%, var(--figure) 100%);
  }
  .brand {
    position: absolute;
    left: 60px;
    top: 42px;
    width: 412px;
    display: flex;
    align-items: center;
    justify-content: center;
    gap: 10px;
    font-size: 34px;
    font-weight: 400;
    color: var(--brand-green);
    line-height: 1;
    white-space: nowrap;
  }
  .brand-dot {
    width: 16px;
    height: 16px;
    border-radius: 50%;
    background: var(--brand-green);
    flex: none;
  }
  .tagline {
    position: absolute;
    left: 40px;
    width: 452px;
    text-align: center;
    font-size: 25px;
    margin: 0;
    line-height: 1;
    white-space: nowrap;
  }
  .tagline--top { top: 118px; }
  .tagline--organic { top: 328px; }
  .tagline--natural { top: 358px; }
  .product-name {
    position: absolute;
    left: 60px;
    top: 168px;
    width: 412px;
    height: 137px;
    display: flex;
    align-items: center;
    justify-content: center;
    margin: 0;
    font-weight: 600;
    font-size: 84px;
    line-height: 1;
    color: var(--name-green);
    white-space: nowrap;
  }
  .capsule-band {
    position: absolute;
    left: 0;
    top: 393px;
    width: 100%;
    height: 47px;
    background: var(--band);
    color: var(--band-text);
    font-size: 22px;
    line-height: 47px;
    padding-left: 140px;
    box-sizing: border-box;
  }
  .ingredients {
    position: absolute;
    left: 697px;
    top: 53px;
    width: 282px;
    height: 337px;
    box-sizing: border-box;
    border: 5px solid var(--frame-green);
    border-radius: 34px;
    outline: 2px solid rgba(47, 168, 74, 0.45);
    outline-offset: -12px;
    background: rgba(255, 255, 255, 0.35);
    text-align: center;
  }
  .ingredients-title {
    margin: 22px 0 12px;
    font-weight: 600;
    font-size: 30px;
    line-height: 1.2;
    color: var(--name-green);
  }
  .ingredients-list {
    list-style: none;
    margin: 0;
    padding: 0;
    font-size: 28px;
    line-height: 38px;
  }
</style>
</head>
<body>
  <main class="label">
    <div class="leaf-canopy" role="img" aria-label="Branches of fresh green leaves along the top edge"></div>
    <div class="figure-area" role="img" aria-label="Faint silhouette of a slim woman behind the product name"></div>

    <div class="brand"><span class="brand-dot"></span><span>Calm Rootwell</span></div>

    <p class="tagline tagline--top">Weight loss alternative</p>

    <h1 class="product-name">Trim 9</h1>

    <p class="tagline tagline--organic">All organic ingredients</p>
    <p class="tagline tagline--natural">All natural</p>

    <section class="ingredients">
      <h2 class="ingredients-title">Contains</h2>
      <ul class="ingredients-list">
        <li>Chia</li>
        <li>Turmeric</li>
        <li>Ginger</li>
        <li>Dandelion</li>
        <li>Macha</li>
        <li>Seaweed</li>
      </ul>
    </section>

    <div class="capsule-band">120 capsules in a packet</div>
  </main>
</body>
</html>
```